Supply Chain Management Site - CrateLogix

We are a supply chain management company that offers the following products:
Warehouse Management System (WMS)
Order Management System (OMS)
Delivery / Fleet Management System

Our product caters to 3PL and distributions.

Ideally a site with a light background would be good.
We like the following sites:
www.venquor.com
http://www.brolvane.com/us/
http://www.tremvik.com/

You can use the content from here:
http://host.sample847.com/demo/crate-logix/

However, we really DO NOT like the design. You DO NOT have to have all the content on the home page. We can have the features and other things on other pages.

Some more content attached.

```html
<!DOCTYPE html>
<html lang="en">
<head>
<meta charset="utf-8">
<title>CrateLogix – Warehouse Management</title>
<link rel="stylesheet" href="https://fonts.googleapis.com/css2?family=Oswald:wght@400;500&family=Roboto:wght@400;500&family=Open+Sans:wght@400;600&display=swap">
<style>
:root{
  --blue:#1f78c8;
  --blue-dark:#1862a8;
  --ink:#333;
  --muted:#555;
  --line:#e6e6e6;
  --panel:#f4f5f6;
  --footer:#0e0f10;
  --footer-text:#9a9a9a;
}
*{margin:0;padding:0;box-sizing:border-box}
html,body{width:722px;height:1200px;overflow:hidden;background:#fff}
body{position:relative;font-family:"Open Sans",Arial,sans-serif;color:var(--ink)}
.abs{position:absolute}
.topbar{left:0;top:0;width:722px;height:2px;background:var(--blue)}
.header{left:0;top:2px;width:722px;height:70px;background:#fff}
.brand{left:59px;top:22px;display:flex;align-items:center;gap:8px}
.brand-name{font-family:"Roboto",sans-serif;font-size:15px;font-weight:500;letter-spacing:1.5px;color:#1c2530}
.brand-dot{width:14px;height:14px;border-radius:50%;background:var(--blue)}
.nav{top:32px;font-family:"Roboto",sans-serif;font-size:10.5px;color:#444}
.nav-sep{top:26px;width:1px;height:22px;background:#eee}
.search{left:557px;top:29px;width:106px;height:22px;border:1px solid #e2e2e2;border-radius:3px;font-size:7px;color:#666;padding:7px 8px}
.search svg{position:absolute;right:7px;top:7px}
.hero{left:0;top:72px;width:722px;height:291px;background:linear-gradient(100deg,#9a8570 0%,#b9a68c 30%,#6f8fb0 55%,#c6ab84 80%,#9e8466 100%)}
.hero-title{left:93px;top:182px;font-family:"Oswald",sans-serif;font-weight:500;font-size:46px;color:#fff;line-height:1}
.hero-sub{left:94px;top:236px;font-family:"Oswald",sans-serif;font-size:21px;color:#fff;line-height:1}
.arrow{top:238px;width:28px;height:28px;border-radius:50%;background:rgba(0,0,0,.25);border:1px solid rgba(255,255,255,.6)}
.band{left:0;top:363px;width:722px;height:71px;background:var(--blue)}
.band-1{left:59px;top:379px;font-family:"Roboto",sans-serif;font-size:12.5px;letter-spacing:.6px;color:#fff}
.band-2{left:59px;top:403px;font-family:"Roboto",sans-serif;font-size:12.5px;letter-spacing:.4px;color:#fff}
.cta{left:559px;top:386px;width:104px;height:26px;background:#fff;border-radius:2px;color:var(--blue);font-family:"Roboto",sans-serif;font-size:10px;text-align:center;line-height:26px}
.intro-title{left:0;top:452px;width:722px;text-align:center;font-family:"Roboto",sans-serif;font-size:19.5px;color:#333}
.intro-text{left:110px;top:484px;width:502px;text-align:center;font-size:6.6px;line-height:13px;color:#555}
.card{top:546px;width:189px}
.card-img{width:189px;height:109px}
.card-title{margin-top:21px;text-align:center;font-family:"Roboto",sans-serif;font-size:9px;color:#222;letter-spacing:.2px}
.card-text{margin-top:8px;text-align:center;font-size:6.2px;line-height:12.4px;color:#555}
.btn{display:block;background:var(--blue);color:#fff;font-family:"Roboto",sans-serif;font-size:6.5px;text-align:center;border-radius:2px;text-decoration:underline}
.card .btn{width:61px;height:20px;line-height:20px;margin:13px auto 0}
.divider{left:59px;top:805px;width:604px;height:1px;background:var(--line)}
.col-title{top:832px;font-family:"Roboto",sans-serif;font-size:12px;color:#222}
.list{top:864px;list-style:none;font-size:7.5px;color:#444}
.list li{height:20px;display:flex;align-items:center;gap:9px}
.list li::before{content:"";width:4px;height:4px;border-radius:50%;border:1.5px solid #333;box-shadow:0 0 0 1px #fff,0 0 0 1.8px #333}
.list + .btn,.col-btn{width:53px;height:19px;line-height:19px;text-decoration:none;font-weight:500}
.more-title{left:399px;top:830px;font-family:"Roboto",sans-serif;font-size:16px;color:#222}
.acc{left:399px;width:264px;height:21px;background:var(--panel);border:1px solid #e4e4e4;font-size:7.2px;color:#333;padding-left:9px;line-height:19px}
.acc-toggle{position:absolute;right:-1px;top:-1px;width:21px;height:21px;border-left:1px solid #e4e4e4;text-align:center;line-height:20px;font-size:11px;color:#d9742b}
.acc.open .acc-toggle{background:var(--blue);color:#fff;border-color:var(--blue)}
.acc-body{left:399px;top:933px;width:264px;height:83px;background:var(--panel);border:1px solid #e4e4e4;border-top:none;padding:14px 14px;font-size:6.4px;line-height:12.4px;color:#555}
.footer{left:0;top:1044px;width:722px;height:156px;background:var(--footer)}
.f-title{top:1057px;font-family:"Roboto",sans-serif;font-size:9.5px;color:#ddd;letter-spacing:.4px}
.tweet{left:59px;width:190px;display:flex;gap:10px;font-size:6.2px;line-height:12px;color:var(--footer-text)}
.tweet i{flex:none;width:11px;height:11px;background:#fff;border-radius:2px;margin-top:1px}
.news-text{left:302px;top:1082px;width:158px;font-size:6.2px;line-height:12px;color:#8a8a8a;text-align:justify}
.news-input{left:302px;top:1115px;width:111px;height:23px;border:1px solid #2a2a2a;background:#0e0f10;font-size:6.2px;color:#666;padding:7px 8px}
.news-btn{left:413px;top:1115px;width:48px;height:23px;background:var(--blue);color:#fff;font-family:"Roboto",sans-serif;font-size:9.5px;text-align:center;line-height:23px}
.contact{left:543px;display:flex;gap:10px;font-size:7px;line-height:12px;color:var(--footer-text);letter-spacing:.3px}
.contact svg{flex:none}
.f-line{left:59px;top:1162px;width:604px;height:1px;background:#1f2022}
.copyright{left:60px;top:1178px;font-size:6.2px;color:#888}
.social{top:1172px;width:17px;height:17px;border-radius:50%;border:1px solid #888}
</style>
</head>
<body>
<div class="abs topbar"></div>
<header class="abs header"></header>
<div class="abs brand"><span class="brand-name">CRATELOGIX</span><span class="brand-dot"></span></div>
<nav>
  <span class="abs nav" style="left:305px">Home</span>
  <span class="abs nav-sep" style="left:346px"></span>
  <span class="abs nav" style="left:362px">About Us</span>
  <span class="abs nav-sep" style="left:418px"></span>
  <span class="abs nav" style="left:434px">Features</span>
  <span class="abs nav-sep" style="left:486px"></span>
  <span class="abs nav" style="left:501px">Contact</span>
</nav>
<div class="abs search">Search
  <svg width="7" height="7" viewBox="0 0 10 10"><circle cx="4" cy="4" r="3" fill="none" stroke="#333" stroke-width="1.6"/><line x1="6.3" y1="6.3" x2="9.2" y2="9.2" stroke="#333" stroke-width="1.6"/></svg>
</div>

<section class="abs hero" role="img" aria-label="Smiling warehouse worker with headset holding a tablet in a shelving aisle"></section>
<div class="abs hero-title">CRATELOGIX</div>
<div class="abs hero-sub">AGILE, DEPENDABLE, SCALABLE</div>
<div class="abs arrow" style="left:23px"><svg width="28" height="28" viewBox="0 0 28 28"><path d="M16 8 L10 14 L16 20" fill="none" stroke="#fff" stroke-width="2.5"/></svg></div>
<div class="abs arrow" style="left:676px"><svg width="28" height="28" viewBox="0 0 28 28"><path d="M12 8 L18 14 L12 20" fill="none" stroke="#fff" stroke-width="2.5"/></svg></div>

<section class="abs band"></section>
<div class="abs band-1">WHAT A WAREHOUSE MANAGEMENT SYSTEM SHOULD BE</div>
<div class="abs band-2">Check out our options and features included</div>
<a class="abs cta">Get Started Now!</a>

<h1 class="abs intro-title" style="font-weight:400">What a Warehouse Management System Should Be</h1>
<p class="abs intro-text">Vestibulum commodo volutpat a, convallis ac, laoreet enim. Phasellus fermentum in, dolor pellentesque. Mulla imperdiet sit amet magna. Vestibulum dapibus, Vestibulum commodo volutpat a, convallis ac, laoreet enim. Phasellus fermentum in, dolor pellentesque. Mulla imperdiet sit amet magna. Vestibulum dapibus, Vestibulum commodo volutpat a, convallis ac, laoreet enim. Phasellus fermentum in,</p>

<article class="abs card" style="left:59px">
  <div class="card-img" role="img" aria-label="Warehouse aisle with tall blue and yellow racking" style="background:linear-gradient(180deg,#5a6f9e,#b4a58a 70%,#c9c5bb)"></div>
  <h3 class="card-title" style="font-weight:400">WAREHOUSE MANAGEMENT SYSTEM</h3>
  <p class="card-text">Lorem ipsum dolor sit amet, consec teer adipiscing. Prsent vestibulum molestie la my hendrerit. mauris haselllus. Porta. Lorem ipsum dolor sit amet, consec</p>
  <a class="btn">LEARN MORE</a>
</article>
<article class="abs card" style="left:266px">
  <div class="card-img" role="img" aria-label="Warehouse worker with clipboard beside cardboard boxes" style="background:linear-gradient(180deg,#8a3a22,#9bb2d0 55%,#b8916a)"></div>
  <h3 class="card-title" style="font-weight:400">ORDER MANAGEMENT SYSTEM</h3>
  <p class="card-text">Lorem ipsum dolor sit amet, consec teer adipiscing. Prsent vestibulum molestie la my hendrerit. mauris haselllus. Porta. Lorem ipsum dolor sit amet, consec</p>
  <a class="btn">LEARN MORE</a>
</article>
<article class="abs card" style="left:474px">
  <div class="card-img" role="img" aria-label="Courier handing a parcel to a customer beside a delivery van" style="background:linear-gradient(180deg,#dfe3e6,#c9cfd4 50%,#b89a74)"></div>
  <h3 class="card-title" style="font-weight:400">DELIVERY / FLEET MANAGEMENT SYSTEM</h3>
  <p class="card-text">Lorem ipsum dolor sit amet, consec teer adipiscing. Prsent vestibulum molestie la my hendrerit. mauris haselllus. Porta. Lorem ipsum dolor sit amet, consec</p>
  <a class="btn">LEARN MORE</a>
</article>

<div class="abs divider"></div>

<h2 class="abs col-title" style="left:60px;font-weight:400">MAJOR BENEFITS</h2>
<ul class="abs list" style="left:60px">
  <li>Improve customer satisfaction</li>
  <li>Barcoding and location tracking</li>
  <li>Reduce labor costs</li>
  <li>Picking and receiving efficiencies</li>
  <li>Better product accountability</li>
  <li>Paperless</li>
</ul>
<a class="abs btn col-btn" style="left:60px;top:987px">READ MORE</a>

<h2 class="abs col-title" style="left:232px;font-weight:400">KEY FEATURES</h2>
<ul class="abs list" style="left:232px">
  <li>Improve customer satisfaction</li>
  <li>Barcoding and location tracking</li>
  <li>Reduce labor costs</li>
  <li>Picking and receiving efficiencies</li>
  <li>Better product accountability</li>
  <li>Paperless</li>
</ul>
<a class="abs btn col-btn" style="left:232px;top:987px">READ MORE</a>

<h2 class="abs more-title" style="font-weight:400">More Features</h2>
<div class="abs acc" style="top:861px">Forecasting &amp; Price Elasticity<span class="acc-toggle">+</span></div>
<div class="abs acc" style="top:887px">Omni-Channel<span class="acc-toggle">+</span></div>
<div class="abs acc open" style="top:913px">Analytics Case Studies<span class="acc-toggle">–</span></div>
<div class="abs acc-body">Lorem ipsum dolor sit amet, consectetur adipiscing elit, sed do eiusmod tempor incididunt ut labore et dolore magna aliqua. Ut enim ad minim veniam, quis nostrud exercitation ullamco laboris nisi ut aliquip ex ea commodo consequat.</div>

<footer class="abs footer"></footer>
<h4 class="abs f-title" style="left:59px;font-weight:400">LATEST TWEET`S</h4>
<div class="abs tweet" style="top:1078px"><i></i><span>Good morning .... wherever you are today! All of us at ...See more here http://t.co/Qx7Lm2Rv0a</span></div>
<div class="abs tweet" style="top:1114px"><i></i><span>Good morning .... wherever you are today! All of us at ...See more here http://t.co/Qx7Lm2Rv0a</span></div>

<h4 class="abs f-title" style="left:302px;top:1060px;font-weight:400">NEWSLETTER</h4>
<p class="abs news-text">Excepteur sint occaecat cupidatat non proident, sunt in culpa qui officia deserunt mollit anim</p>
<div class="abs news-input">Enter your email address</div>
<div class="abs news-btn">Sign Up</div>

<h4 class="abs f-title" style="left:543px;top:1054px;font-weight:400">CONTACT US</h4>
<div class="abs contact" style="top:1077px">
  <svg width="8" height="11" viewBox="0 0 8 11"><path d="M4 0.5a3.5 3.5 0 0 1 3.5 3.5C7.5 6.5 4 10.5 4 10.5S0.5 6.5 0.5 4A3.5 3.5 0 0 1 4 0.5z" fill="#9a9a9a"/><circle cx="4" cy="4" r="1.3" fill="#0e0f10"/></svg>
  <span>1820 Harbor Point Rd. North<br>Millbrook, NJ</span>
</div>
<div class="abs contact" style="top:1109px">
  <svg width="10" height="10" viewBox="0 0 10 10"><path d="M2 1 L3.5 1 L4.3 3 L3.2 4 Q4.3 6 6 6.8 L7 5.7 L9 6.5 L9 8 Q9 9 8 9 Q1 8.5 1 2 Q1 1 2 1z" fill="none" stroke="#9a9a9a" stroke-width=".9"/></svg>
  <span>555 014 2290</span>
</div>
<div class="abs contact" style="top:1127px">
  <svg width="11" height="9" viewBox="0 0 11 9"><rect x=".5" y=".5" width="10" height="8" fill="none" stroke="#9a9a9a"/><path d="M.5 .5 L5.5 5 L10.5 .5" fill="none" stroke="#9a9a9a"/></svg>
  <span>hello@quarvenmail.com</span>
</div>

<div class="abs f-line"></div>
<div class="abs copyright">© 2015 CRATELOGIX - All Rights Reserved</div>
<span class="abs social" style="left:599px"></span>
<span class="abs social" style="left:623px"></span>
<span class="abs social" style="left:647px"></span>
</body>
</html>
```